Sci Fi/ Secret Agent Author needs website design!

My name is Talia Brook and I am an author. I require a site that can provide information about myself and my books and other works.

I would like it to have a Home, blog function, (about the) books/series section so people can visit another section and read about each individual book that's going to be released. A resources page, a Store, social media links and ability to load/embed videos from clipvana and other.

I write mild scifi/thriller/conspiracy/secret government type novels. -At the moment-. The series follows a strong female lead that is an agent with a secret organisation in a classified military installation.

The theme would be professional yet possibly show this element.

Target Market(s)

/military fiction/thriller/fantasy/Sci fi/ femme-fatal, readers. Mostly females, age 18-60
Novel readers

Number of Pages Required

5+ page

Requirements
Must have
• Would like designers to follow brief. :)
• My budget includes all the pages I will need;
• eg home, blog, resources, store, ability to pay with coinlark and Credit Cards
• , ability to have trailers from clipvana etc. Must have links to the social media mentioned in the brief.
Nice to have
• use of the colours I have suggested. electric/indigo purple, fuschia highlights , dark greys
• as I will possibly base branding for social media ETC on the look of your website design and colour scheme.
• Ability for trailer on front page??
Should not have
• Should not be too cluttered. (But I am open to all ideas)

```html
<!DOCTYPE html>
<html lang="en">
<head>
<meta charset="utf-8">
<title>Talia Brook — Author Extraordinaire</title>
<link href="https://fonts.googleapis.com/css2?family=Bebas+Neue&family=Montserrat:wght@400;500&family=Raleway:wght@200&display=swap" rel="stylesheet">
<style>
  :root {
    --ink: #000000;
    --paper: #ffffff;
    --text-light: #e4e4e8;
    --indigo-deep: #250a4f;
    --indigo-band: #2b0c58;
    --violet-bright: #6c2ab4;
    --hero-a: #5a3a9e;
    --hero-b: #3a1f74;
    --video-a: #9370c0;
    --video-b: #67469a;
    --play-a: #7550ab;
    --play-b: #5f3c92;
    --thumb-a: #5a5a5e;
    --thumb-b: #2a2a2e;
    --portrait-a: #5c5c5c;
    --portrait-b: #1e1e1e;
    --tab-friend: #3b5a9a;
    --tab-clip: #d8452e;
    --tab-snap: #9a4fb8;
    --tab-chirp: #3aa0e0;
  }
  * { box-sizing: border-box; margin: 0; padding: 0; }
  html, body { width: 1200px; height: 911px; overflow: hidden; background: var(--paper); }
  body { position: relative; font-family: "Montserrat", sans-serif; color: var(--text-light); }

  .page { position: absolute; background: var(--ink); overflow: hidden; }
  .page--home { left: 4px; top: 4px; width: 578px; height: 906px; }
  .page--continued { left: 608px; top: 67px; width: 580px; height: 843px; }

  .site-header { position: absolute; left: 0; top: 0; width: 100%; height: 95px; text-align: center; }
  .brand-name { position: absolute; top: 26px; width: 100%; font-family: "Bebas Neue", sans-serif; font-size: 40px; line-height: 1; letter-spacing: 0.5px; color: var(--text-light); }
  .brand-tagline { position: absolute; top: 63px; width: 100%; font-size: 8px; letter-spacing: 0.6px; color: var(--text-light); }

  .main-nav { position: absolute; left: 0; top: 95px; width: 100%; height: 26px; background: var(--indigo-band); display: flex; justify-content: center; align-items: center; gap: 14px; font-size: 12px; font-weight: 500; letter-spacing: 1.6px; color: var(--paper); }
  .main-nav .divider { font-weight: 400; }

  .hero { position: absolute; left: 0; top: 121px; width: 100%; height: 363px; background: radial-gradient(circle at 50% 45%, var(--hero-a), var(--hero-b)); }
  .hero-title { position: absolute; top: 140px; width: 100%; text-align: center; font-family: "Bebas Neue", sans-serif; font-size: 64px; line-height: 1; color: var(--text-light); }
  .hero-subtitle { position: absolute; top: 201px; width: 100%; text-align: center; font-family: "Raleway", sans-serif; font-weight: 200; font-size: 29px; letter-spacing: 1px; color: var(--text-light); }

  .trailer { position: absolute; background: linear-gradient(120deg, var(--video-a), var(--video-b)); }
  .page--home .trailer { left: 31px; top: 532px; width: 515px; height: 312px; }
  .page--continued .trailer { left: 33px; top: 0; width: 515px; height: 283px; }
  .play-button { position: absolute; width: 212px; height: 149px; border-radius: 34px; background: linear-gradient(180deg, var(--play-a), var(--play-b)); }
  .page--home .play-button { left: 151px; top: 82px; }
  .page--continued .play-button { left: 151px; top: 53px; }
  .play-button svg { position: absolute; left: 83px; top: 42px; }

  .book-cover { position: absolute; width: 162px; height: 108px; background: radial-gradient(circle, var(--thumb-a), var(--thumb-b)); }
  .page--home .book-cover { top: 876px; height: 30px; }
  .book { position: absolute; top: 316px; width: 162px; }
  .book .book-cover { position: relative; }
  .book-title { margin-top: 10px; padding-left: 22px; font-family: "Bebas Neue", sans-serif; font-size: 34px; line-height: 1; color: var(--text-light); }
  .book-desc { padding-left: 22px; font-size: 8px; letter-spacing: 0.3px; }

  .about { position: absolute; left: 0; top: 515px; width: 100%; height: 304px; background: var(--indigo-deep); }
  .about-portrait { position: absolute; left: 33px; top: 20px; width: 217px; height: 265px; background: linear-gradient(160deg, var(--portrait-a), var(--portrait-b)); }
  .about-heading { position: absolute; left: 279px; top: 22px; font-family: "Bebas Neue", sans-serif; font-size: 34px; line-height: 1; color: var(--text-light); }
  .about-text { position: absolute; left: 279px; top: 81px; font-size: 8px; letter-spacing: 0.3px; }

  .footer-band { position: absolute; left: 0; top: 819px; width: 100%; height: 24px; background: var(--violet-bright); }

  .social-tabs { position: absolute; right: 0; top: 691px; display: flex; flex-direction: column; align-items: flex-end; }
  .social-tab { height: 27px; padding: 0 6px; font-size: 8px; font-weight: 500; line-height: 27px; color: var(--paper); }
  .social-tab--friend { background: var(--tab-friend); }
  .social-tab--clip { background: var(--tab-clip); }
  .social-tab--snap { background: var(--tab-snap); }
  .social-tab--chirp { background: var(--tab-chirp); }
</style>
</head>
<body>

<section class="page page--home">
  <header class="site-header">
    <div class="brand-name">TALIA BROOK</div>
    <div class="brand-tagline">AUTHOR EXTRAORDINAIRE</div>
  </header>
  <nav class="main-nav">
    <span>HOME</span><span class="divider">/</span>
    <span>BLOG</span><span class="divider">/</span>
    <span>ABOUT</span><span class="divider">/</span>
    <span>RESOURCES</span><span class="divider">/</span>
    <span>SHOP</span>
  </nav>
  <div class="hero" role="img" aria-label="Purple-toned photo looking down a spiral stairwell with a network line overlay">
    <div class="hero-title">REIMAGINING</div>
    <div class="hero-subtitle">SCI-FI THRILLERS</div>
  </div>
  <div class="trailer" aria-label="Book trailer video player">
    <div class="play-button">
      <svg width="72" height="76" viewBox="0 0 72 76"><polygon points="0,0 72,38 0,76" fill="#ffffff"/></svg>
    </div>
  </div>
  <div class="book-cover" style="left:31px" role="img" aria-label="Book cover image"></div>
  <div class="book-cover" style="left:208px" role="img" aria-label="Book cover image"></div>
  <div class="book-cover" style="left:385px" role="img" aria-label="Book cover image"></div>
</section>

<section class="page page--continued">
  <div class="trailer" aria-label="Book trailer video player">
    <div class="play-button">
      <svg width="72" height="76" viewBox="0 0 72 76"><polygon points="0,0 72,38 0,76" fill="#ffffff"/></svg>
    </div>
  </div>
  <div class="book" style="left:33px">
    <div class="book-cover" role="img" aria-label="Book cover image"></div>
    <div class="book-title">BOOK</div>
    <div class="book-desc">DESCRIPTION</div>
  </div>
  <div class="book" style="left:210px">
    <div class="book-cover" role="img" aria-label="Book cover image"></div>
    <div class="book-title">BOOK</div>
    <div class="book-desc">DESCRIPTION</div>
  </div>
  <div class="book" style="left:386px">
    <div class="book-cover" role="img" aria-label="Book cover image"></div>
    <div class="book-title">BOOK</div>
    <div class="book-desc">DESCRIPTION</div>
  </div>
  <div class="about">
    <div class="about-portrait" role="img" aria-label="Black and white author portrait"></div>
    <div class="about-heading">ABOUT ME</div>
    <div class="about-text">DESCRIPTION</div>
  </div>
  <div class="footer-band"></div>
  <div class="social-tabs">
    <span class="social-tab social-tab--friend">Friendloop</span>
    <span class="social-tab social-tab--clip">clipvana</span>
    <span class="social-tab social-tab--snap">Snapora</span>
    <span class="social-tab social-tab--chirp">Chirpline</span>
  </div>
</section>

</body>
</html>
```